Gazebo 3x3m design

I would require design/branding for Gazebo with size 3x3 meters for company called Pan Full Sizzle. This would be for Korean style Con Dogs using attached already designed cartoon characters (corn dog and cake Pan Full Sizzle), but making design to stand out, attractive and eye catching. Design requires to cover these as per attached example of different style of Gazebo branding:

Use attached characters with wording Pan Full Sizzle Korean Corn Dogs & Lovelies (not & more)
2x 2 meter high and 3 meter wide walls
2x 1 meter high and 3 meter wide half walls
1x canopy design (exact measurements in API file will be sent to the final designer)

The font with the cartoon Characters is not necessary required. Please provide font that Suits your design best. Also It should sat Crispy Corn Dogs & Sweet Bites (not & more).

In addition to Corn Dogs, we do sell sweets Pan Full Sizzle, it would be great to incorporate these in the walls somehow, please see examples in attachement.

Target Market(s)

Food Markets

Industry/Entity Type

Food

Colors
59FF00
82FF00
B8FF75
E3FFCB
F4FFEA
EE7325
F08F49
F5BC92
FAE3D3
FDF4ED
EB3D1F
EC4F4E
F09395
F8D3D4
FCEDEE

Requirements
Must have
• Cartoon Characters attached
Nice to have
• Stand out design

```html
<!DOCTYPE html>
<html lang="en">
<head>
<meta charset="utf-8">
<title>Pan Full Sizzle – Gazebo 3x3m Branding</title>
<link href="https://fonts.googleapis.com/css2?family=Fredoka:wght@600&family=Quicksand:wght@700&display=swap" rel="stylesheet">
<style>
  :root{
    --bg:#d9d9d9;
    --canopy:#e8401f;
    --canopy-dark:#cf3418;
    --wall-red:#d63a3c;
    --wall-deep:#b8272c;
    --wall-light:#f09395;
    --wall-pale:#f8d3d4;
    --brand-gold:#f0ad3a;
    --ink:#6e1a1c;
    --photo-ring:#fcedee;
    --photo-food:#d98a3a;
    --photo-sweet:#b98a80;
    --char:#c98a4a;
  }
  *{box-sizing:border-box;margin:0;padding:0}
  html,body{width:1200px;height:900px;overflow:hidden;background:var(--bg)}
  body{position:relative;font-family:"Quicksand",sans-serif}

  .brand-name{font-family:"Fredoka",sans-serif;font-weight:600;color:var(--brand-gold);line-height:.95;text-transform:lowercase}
  .tagline{font-family:"Quicksand",sans-serif;font-weight:700;color:var(--ink);white-space:nowrap}

  .canopy-roof{position:absolute;left:250px;top:24px;width:700px;height:170px}
  .canopy-roof .roof-logo{position:absolute;left:220px;top:68px;display:flex;align-items:center;gap:14px}
  .canopy-roof .roof-name{font-size:40px;width:190px}
  .canopy-roof .roof-tag{position:absolute;left:330px;top:148px;font-size:13px}

  .character{background:linear-gradient(160deg,var(--char),#8a4a30);border-radius:40% 40% 30% 30%}

  .valance{position:absolute;left:100px;top:198px;width:1000px;height:58px;background:var(--canopy);
    display:flex;align-items:center;justify-content:space-between;padding:0 26px}
  .valance .brand-name{font-size:22px;width:96px}
  .valance .tagline{font-size:30px}

  .wall{position:absolute;overflow:hidden;
    background:radial-gradient(circle at 40% 55%,var(--wall-pale) 0%,var(--wall-light) 35%,var(--wall-red) 70%,var(--wall-deep) 100%)}
  .wall-full{width:480px;height:320px;top:280px}
  .wall-a{left:100px}
  .wall-b{left:620px}
  .wall-half{left:360px;top:628px;width:480px;height:160px;background:linear-gradient(90deg,var(--wall-deep),var(--wall-red) 50%,var(--wall-deep))}

  .photo{position:absolute;border-radius:50%;border:4px solid var(--photo-ring)}
  .photo-food{background:radial-gradient(circle,#e7a04a,var(--photo-food) 55%,#f4d6c4 80%)}
  .photo-sweet{background:radial-gradient(circle,#e9c3c0,var(--photo-sweet) 55%,#f4dcdc 80%)}

  .social-row{position:absolute;bottom:12px;left:0;right:0;display:flex;justify-content:space-around}
  .social-item{display:flex;align-items:center;gap:6px}
  .social-item .dot{width:16px;height:16px;border-radius:50%;background:var(--ink)}
  .social-item .brand-name{font-size:13px;width:48px}
</style>
</head>
<body>

  <div class="canopy-roof">
    <svg width="700" height="170" viewBox="0 0 700 170">
      <polygon points="350,0 700,170 0,170" fill="var(--canopy)"/>
      <polygon points="350,0 700,170 350,170" fill="var(--canopy-dark)" opacity=".25"/>
    </svg>
    <div class="roof-logo">
      <div class="character" role="img" aria-label="Cartoon corn dog and cake characters" style="width:110px;height:72px"></div>
      <div class="brand-name roof-name">Pan Full Sizzle</div>
    </div>
    <div class="tagline roof-tag">Crispy Corn Dogs &amp; Sweet Bites</div>
  </div>

  <div class="valance">
    <div class="brand-name">Pan Full Sizzle</div>
    <div class="tagline">Crispy Corn Dogs &amp; Sweet Bites</div>
    <div class="brand-name">Pan Full Sizzle</div>
  </div>

  <section class="wall wall-full wall-a">
    <div class="photo photo-sweet" role="img" aria-label="Photo of chocolate dipped sweets" style="left:18px;top:18px;width:100px;height:100px"></div>
    <div class="photo photo-food" role="img" aria-label="Photo of corn dogs with ketchup" style="right:18px;top:14px;width:100px;height:130px"></div>
    <div class="character" role="img" aria-label="Cartoon corn dog and cake characters" style="position:absolute;left:100px;top:120px;width:110px;height:130px"></div>
    <div class="brand-name" style="position:absolute;left:220px;top:150px;font-size:48px;width:170px">Pan Full Sizzle</div>
    <div class="tagline" style="position:absolute;left:220px;top:252px;font-size:13px">Crispy Corn Dogs &amp; Sweet Bites</div>
    <div class="social-row">
      <div class="social-item"><span class="dot"></span><span class="brand-name">Pan Full Sizzle</span></div>
      <div class="social-item"><span class="dot"></span><span class="brand-name">Pan Full Sizzle</span></div>
      <div class="social-item"><span class="dot"></span><span class="brand-name">Pan Full Sizzle</span></div>
    </div>
  </section>

  <section class="wall wall-full wall-b">
    <div class="photo photo-food" role="img" aria-label="Photo of corn dogs with ketchup" style="right:40px;top:22px;width:160px;height:120px"></div>
    <div class="brand-name" style="position:absolute;left:40px;top:150px;font-size:52px;width:260px">Pan Full Sizzle</div>
    <div class="tagline" style="position:absolute;left:40px;top:262px;font-size:15px">Crispy Corn Dogs &amp; Sweet Bites</div>
    <div class="social-row" style="justify-content:space-between;padding:0 40px">
      <div class="social-item"><span class="dot"></span><span class="brand-name">Pan Full Sizzle</span></div>
      <div class="social-item"><span class="dot"></span><span class="brand-name">Pan Full Sizzle</span></div>
    </div>
  </section>

  <section class="wall wall-half">
    <div class="photo photo-food" role="img" aria-label="Photo of corn dogs with ketchup" style="left:14px;top:12px;width:60px;height:90px"></div>
    <div class="brand-name" style="position:absolute;left:130px;top:22px;font-size:34px;width:150px">Pan Full Sizzle</div>
    <div class="tagline" style="position:absolute;left:130px;top:98px;font-size:10px">Crispy Corn Dogs &amp; Sweet Bites</div>
    <div class="character" role="img" aria-label="Cartoon corn dog and cake characters" style="position:absolute;left:295px;top:10px;width:80px;height:110px"></div>
    <div class="photo photo-sweet" role="img" aria-label="Photo of chocolate dipped sweets" style="right:14px;top:18px;width:60px;height:70px"></div>
    <div class="social-row" style="bottom:8px">
      <div class="social-item"><span class="dot" style="width:11px;height:11px"></span><span class="brand-name" style="font-size:10px;width:36px">Pan Full Sizzle</span></div>
      <div class="social-item"><span class="dot" style="width:11px;height:11px"></span><span class="brand-name" style="font-size:10px;width:36px">Pan Full Sizzle</span></div>
      <div class="social-item"><span class="dot" style="width:11px;height:11px"></span><span class="brand-name" style="font-size:10px;width:36px">Pan Full Sizzle</span></div>
    </div>
  </section>

</body>
</html>
```